A4 Brochure Creation - Exciting Product

I want something designed for a new breakthrough product
I have attached an example of another product design done Infrared Thermomoter
But I want this one looking much much more professional than that example

I want it to be a quick easy to understand brochure powerful on the ability to report by cloud

Target Market(s)

Pubs Clubs Business AgedCare anyone with people entering

Industry/Entity Type

Security Device

Colors
00a990
0792cd

Requirements
Must have
• Applicable to Entrances in Aged Care, hotels, office buildings, schools, shopping malls, shops, communities, public services and management projects that need to use face access to control access and health keeping.

Secure Door Control by easily interfacing to the output relay ensuring only visitors or staff with body temperatures within normal range to gain access.

Payroll Sign In Systems which include existing fingerprint scanning technologies can easily be interfaced ensuring all staff member are within safe temperature ranges before commencing their shits.

Blacklisting is available by our cloud application ensuring someone whom does not have any authority to ever enter a building will not gain access when interfaced to the access control system.
Nice to have
• Executives and Decision makers to be wowed
Should not have
• No flow

```html
<!DOCTYPE html>
<html lang="en">
<head>
<meta charset="utf-8">
<title>Veritherm Health – Facial Recognition with Thermal Imaging</title>
<link rel="stylesheet" href="https://fonts.googleapis.com/css2?family=Poppins:wght@500;600;700;800&family=Roboto:ital,wght@0,400;0,500;0,700;1,400;1,500&display=swap">
<style>
  :root {
    --page-bg: #e4e4e4;
    --paper: #f4f4f4;
    --ink: #2a2a2a;
    --green: #4f9f45;
    --green-dark: #3f8d36;
    --blue: #2673b5;
    --blue-ring: #2a6fb0;
    --bar: #2b2b2b;
    --arc: #dcdcdc;
    --white: #ffffff;
  }
  * { box-sizing: border-box; margin: 0; padding: 0; }
  html, body { width: 1135px; height: 1200px; overflow: hidden; background: var(--page-bg); }
  .stage { position: relative; width: 1135px; height: 1200px; }
  .flyer {
    position: absolute; left: 148px; top: 0;
    width: 788px; height: 1127px;
    transform: scale(1.0648); transform-origin: top left;
    background: var(--paper); overflow: hidden;
    font-family: "Roboto", Arial, sans-serif; color: var(--ink);
  }
  .abs { position: absolute; }

  /* brand */
  .brand { left: 55px; top: 48px; display: flex; align-items: center; gap: 12px; }
  .brand-dot { width: 40px; height: 40px; border-radius: 50%; background: var(--green); }
  .brand-name { font-family: "Poppins", sans-serif; font-weight: 600; font-size: 40px; color: var(--green); letter-spacing: -0.5px; line-height: 1; }
  .brand-tagline { left: 127px; top: 108px; font-family: "Roboto", sans-serif; font-style: italic; font-weight: 700; font-size: 17px; color: var(--green); }

  /* hero */
  .headline { left: 43px; top: 158px; font-family: "Poppins", sans-serif; font-size: 45px; line-height: 50px; letter-spacing: 0.5px; text-transform: uppercase; }
  .headline .light { font-weight: 500; display: block; }
  .headline .bold { font-weight: 800; display: block; }
  .tag-banner { left: 43px; top: 407px; width: 358px; height: 25px; background: var(--green); color: var(--white); font-style: italic; font-size: 12px; line-height: 25px; padding-left: 6px; }
  .symptoms { left: 44px; top: 440px; font-style: italic; font-weight: 500; font-size: 15.5px; }

  .arc { left: 543px; top: 27px; width: 480px; height: 480px; border-radius: 50%; border: 8px solid var(--arc); }
  .thermal { left: 660px; top: 65px; width: 140px; height: 435px;
    border-radius: 120px 0 0 60px;
    background: linear-gradient(160deg, #f0c020 0%, #e8261c 22%, #f26d1a 38%, #3a4fb5 55%, #2a3fa8 70%, #e82b1e 88%, #f7d21a 100%); }
  .device-photo { left: 413px; top: 205px; width: 260px; height: 260px; border-radius: 50%; border: 6px solid var(--blue-ring);
    background: radial-gradient(circle at 50% 40%, #6b7279 0%, #4c4f52 45%, #b89a7c 80%, #a48668 100%); }

  /* steps */
  .step { top: 493px; width: 180px; text-align: center; }
  .step-num { width: 48px; height: 48px; margin: 0 auto; border-radius: 50%; background: var(--green); color: var(--white); font-family: "Poppins", sans-serif; font-weight: 500; font-size: 22px; line-height: 48px; }
  .step-label { margin-top: 11px; font-weight: 500; font-size: 13px; line-height: 16px; }
  .step-divider { top: 547px; width: 2px; height: 47px; background: var(--ink); }

  /* panels */
  .panel-head { top: 617px; height: 44px; background: var(--bar); color: var(--white); font-family: "Poppins", sans-serif; font-weight: 600; font-size: 22px; line-height: 42px; }
  .desc-head { left: 0; width: 393px; padding-left: 43px; }
  .feat-head { left: 396px; width: 392px; padding-left: 41px; }
  .desc-body { left: 0; top: 661px; width: 393px; height: 323px; background: var(--green); color: var(--white); padding: 26px 34px 0 43px; font-style: italic; font-size: 11.2px; line-height: 15.4px; }
  .feat-body { left: 396px; top: 661px; width: 392px; height: 323px; background: var(--blue); color: var(--white); padding: 25px 30px 0 40px; font-size: 12.6px; line-height: 16px; }
  .feat-list { list-style: none; }
  .feat-list li { position: relative; padding-left: 23px; margin-bottom: 16px; }
  .feat-list li::before { content: ""; position: absolute; left: 0; top: 5px; width: 7px; height: 7px; border-radius: 50%; background: var(--white); }
  .feat-list b { font-weight: 700; }

  /* suitability */
  .suitable-title { left: 44px; top: 1015px; font-style: italic; font-weight: 500; font-size: 34px; }
  .sector { top: 1006px; width: 80px; text-align: center; }
  .sector svg { display: block; margin: 0 auto; }
  .sector span { display: block; margin-top: 6px; font-style: italic; font-weight: 500; font-size: 12.5px; }

  .footer { left: 0; top: 1083px; width: 788px; height: 44px; background: var(--bar); color: var(--white); text-align: center; font-family: "Poppins", sans-serif; font-weight: 500; font-size: 23px; letter-spacing: 3px; line-height: 46px; }
</style>
</head>
<body>
<div class="stage">
  <div class="flyer">
    <div class="abs brand"><span class="brand-dot"></span><span class="brand-name">Veritherm health</span></div>
    <div class="abs brand-tagline">Specialists in Telecommunication</div>

    <div class="abs arc"></div>
    <div class="abs thermal" role="img" aria-label="Thermal camera image of a person's head in rainbow heat colours"></div>
    <div class="abs device-photo" role="img" aria-label="Photo of the facial recognition thermal terminal on a desk stand"></div>

    <h1 class="abs headline"><span class="light">Facial</span><span class="light">Recognition</span><span class="bold">With</span><span class="bold">Thermal</span><span class="bold">Imaging</span></h1>
    <div class="abs tag-banner">Protection made simple detecting Elevated Body Temperatures</div>
    <div class="abs symptoms">COVID – GASTRO – Flu symptoms plus more</div>

    <div class="abs step" style="left:22px"><div class="step-num">1</div><div class="step-label">Intregrates With Door<br>Access Control Systems</div></div>
    <div class="abs step-divider" style="left:206px"></div>
    <div class="abs step" style="left:206px"><div class="step-num">2</div><div class="step-label">Stranger Warning And<br>Blacklist Management</div></div>
    <div class="abs step-divider" style="left:392px"></div>
    <div class="abs step" style="left:390px"><div class="step-num">3</div><div class="step-label">Proof Of Identitiy<br>For Staff</div></div>
    <div class="abs step-divider" style="left:567px"></div>
    <div class="abs step" style="left:577px"><div class="step-num">4</div><div class="step-label">Non Contact Automatic<br>Temperature Measurement</div></div>

    <div class="abs panel-head desc-head">Product Description</div>
    <div class="abs panel-head feat-head">Key Features</div>
    <div class="abs desc-body">The new AI (artificial intelligence) technology deployed in our technology allows thermal imaging capturing face temperature whether the identifying person is wearing a face mask or not. Detection via this intelligent terminal integrates face detection and temperature measurement integrating facial contrast recognition, heating imaging via our contactless temperature measurement module. When the person to be identified engages the face recognition terminal, the human body surface temperature can be measured by the thermal imaging technology. The whole face recognition process is a non-contact experience, and is accurate, reliable, efficient and adds an enormous level of safety to your facility. If the temperature of the detected person exceeds a certain threshold, the signal light of the terminal will send out an abnormal warning and carry out a voice warning. Images are captured successful or non-successful and stored in a secure managed onsite database if chosen by the customer deploying the product.</div>
    <div class="abs feat-body">
      <ul class="feat-list">
        <li><b>Measurement Distance:</b> 50 – 150cm</li>
        <li><b>Camera:</b> 2 Mega Pixels Binocular wide dynamic</li>
        <li><b>Tablet Screen:</b> 8.0 Inch LCD Screen<br>Network: WiFi and Ethernet</li>
        <li>20,000 Photo Database</li>
        <li>Manage Contractors, Staff and log visitors as strangers</li>
        <li>Integrate to existing Access Control, Fingerprint Scanners and other devices for management</li>
        <li>Wall Mount, Desk Mount and Tripod Mounts available</li>
      </ul>
    </div>

    <div class="abs suitable-title">Suitable for</div>
    <div class="abs sector" style="left:290px"><svg width="40" height="40" viewBox="0 0 40 40"><circle cx="20" cy="20" r="18" fill="none" stroke="var(--blue)" stroke-width="2.5"/><path d="M12 20.5l5.5 5.5 11-12" fill="none" stroke="var(--blue)" stroke-width="2.5" stroke-linecap="round" stroke-linejoin="round"/></svg><span>Aged Care</span></div>
    <div class="abs sector" style="left:366px"><svg width="40" height="40" viewBox="0 0 40 40"><circle cx="20" cy="20" r="18" fill="none" stroke="var(--blue)" stroke-width="2.5"/><path d="M12 20.5l5.5 5.5 11-12" fill="none" stroke="var(--blue)" stroke-width="2.5" stroke-linecap="round" stroke-linejoin="round"/></svg><span>Hospitals</span></div>
    <div class="abs sector" style="left:442px"><svg width="40" height="40" viewBox="0 0 40 40"><circle cx="20" cy="20" r="18" fill="none" stroke="var(--blue)" stroke-width="2.5"/><path d="M12 20.5l5.5 5.5 11-12" fill="none" stroke="var(--blue)" stroke-width="2.5" stroke-linecap="round" stroke-linejoin="round"/></svg><span>Hotels</span></div>
    <div class="abs sector" style="left:518px"><svg width="40" height="40" viewBox="0 0 40 40"><circle cx="20" cy="20" r="18" fill="none" stroke="var(--blue)" stroke-width="2.5"/><path d="M12 20.5l5.5 5.5 11-12" fill="none" stroke="var(--blue)" stroke-width="2.5" stroke-linecap="round" stroke-linejoin="round"/></svg><span>Offices</span></div>
    <div class="abs sector" style="left:593px"><svg width="40" height="40" viewBox="0 0 40 40"><circle cx="20" cy="20" r="18" fill="none" stroke="var(--blue)" stroke-width="2.5"/><path d="M12 20.5l5.5 5.5 11-12" fill="none" stroke="var(--blue)" stroke-width="2.5" stroke-linecap="round" stroke-linejoin="round"/></svg><span>Schools</span></div>
    <div class="abs sector" style="left:670px"><svg width="40" height="40" viewBox="0 0 40 40"><circle cx="20" cy="20" r="18" fill="none" stroke="var(--blue)" stroke-width="2.5"/><path d="M12 20.5l5.5 5.5 11-12" fill="none" stroke="var(--blue)" stroke-width="2.5" stroke-linecap="round" stroke-linejoin="round"/></svg><span>Workplaces</span></div>

    <div class="abs footer">020 555 0148 &nbsp;|&nbsp; www.verithermhealth.com</div>
  </div>
</div>
</body>
</html>
```